Speisekarten-Design für mediterranes Restaurant
Zielgruppe
Wir eröffnen am 23.09.2022 ein Restaurant im Hotel SolBrunn Bad Farnhain in 94999 Fürstenzell unter dem Namen 'VELO'. Die Übersetzung aus dem Portugiesischem bedeutet 'Seele' - Velo soll also die Seele des Hauses werden und unsere Gäste aus nah&fern und ob jung oder alt mit mediterranen, besonderen Köstlichkeiten unseres Küchenchefs Matteo Carvalhal verwöhnen.
Auf der Speisekarte stehen Bruch & Frühstück (z.B. Joghurt mit Früchten und Agavensirup, Pancakes und Waffeln, Egg Benedikt aber auch bayerische Spezialitäten wie Weißwurst mit Breze). Weiterhin werden wir Tapas (vegatarisch, Fleisch, Fisch) anbieten. Als USP steht die original portugiesische Cataplana oder Hähnchen nach Art des Hauses auf der Karte. Hinzu kommen noch Desserts. Ebenso benötigen wir eine Wochenkarte sowie eine Getränkekarte (Softdrinks, Kaffee, Tee, Bier, Wein, Long Drinks, etc.) Ich denke eine Seite sollte für Frühstück/Brunch und eine für Vorspeisen, Tapas, Hauptspeisen vorgesehen werden und ein Blatt für die Wochenkarte. Weiterhin ein Blatt mit normalen Getränken und eine Weinkarte.
Wir suchen ein modernes, zeitloses Design für unsere neue Speisekarte. Diese soll auf einzelnen Blättern in einem Klemmbrett aus Holz eingespannt werden. Wichtig ist uns, dass wir die Gerichte und Getränke jederzeit in einem festen Design ändern und selbst drucken können.
Die hochgeladenen Speisekarten im Word-Format dienen nur der Orientierung für Anzahl, etc. Die Karten müssen selbstständig durch uns ergänzt oder geändert werden können. Anbei auch ein Beispielbild, welches über entwurfmarkt.de in Bildwand gefunden wurde.
Aufgabenstellung
als DIN-Format wählen wir A4.
Gerichte wir die Cataplana sollten eine Erklärung beinhalten, die auch noch gut aussieht und nicht nur in Klammern unter dem Gericht steht.

```html
<!DOCTYPE html>
<html lang="de">
<head>
<meta charset="utf-8">
<title>VELO – Speisekarte</title>
<link rel="stylesheet" href="https://fonts.googleapis.com/css2?family=Jost:wght@300;400;500&display=swap">
<style>
:root{
  --backdrop:#e4e4e1;
  --sheet:#1c1c1e;
  --ink:#ededeb;
  --ink-soft:#c9c9c6;
  --gold:#b8996a;
}
*{box-sizing:border-box;margin:0;padding:0}
html,body{width:1200px;height:801px;overflow:hidden;background:var(--backdrop)}
body{font-family:'Jost',sans-serif;color:var(--ink);position:relative}
.sheet{position:absolute;top:20px;width:537px;height:760px;background:var(--sheet);overflow:hidden}
.sheet--tapas{left:48px}
.sheet--main{left:615px}
.photo{position:absolute;z-index:0}
.sheet-title{position:absolute;left:0;right:0;text-align:center;font-weight:300;font-size:39px;letter-spacing:.5px;line-height:1}
.title-rule{position:absolute;height:1px;background:var(--gold)}
.hours{position:absolute;left:0;right:0;text-align:center;font-size:13px;font-weight:300;text-decoration:underline;text-underline-offset:2px}
.col{position:absolute;z-index:2}
.section{font-size:12.5px;font-weight:400;text-decoration:underline;text-underline-offset:2px;margin:8px 0 4px;letter-spacing:.2px}
.section:first-child{margin-top:0}
.item{display:flex;justify-content:space-between;font-size:12px;font-weight:300;line-height:1.12}
.item .price{flex:none;padding-left:6px}
.item--small{font-size:10.5px}
.desc{font-size:6.4px;font-weight:300;color:var(--ink-soft);line-height:1.2;margin-bottom:2px}
.gap{height:8px}
.gap--tight{height:6px}
.note{font-size:12px;font-weight:300;line-height:1.15}
</style>
</head>
<body>

<section class="sheet sheet--tapas" aria-label="Tapas &amp; Brotzeit">
  <div class="photo" role="img" aria-label="Foto: Burrata mit Tomaten und Basilikum auf dunklem Teller" style="left:134px;top:0;width:268px;height:176px;background:radial-gradient(ellipse 60px 50px at 45% 60%,#f2efe8 0%,#d9d3c6 60%,transparent 100%),radial-gradient(circle at 62% 20%,#b33c2c 0 14px,transparent 16px),linear-gradient(160deg,#2f4452,#1c2a33)"></div>
  <h1 class="sheet-title" style="top:186px">Tapas &amp; Brotzeit</h1>
  <div class="title-rule" style="left:140px;width:256px;top:232px"></div>
  <p class="hours" style="top:237px">Von 16:00 bis 22:00 Uhr</p>

  <div class="col" style="left:72px;top:270px;width:152px">
    <h2 class="section">VORSPEISEN</h2>
    <div class="item"><span>Tagessuppe</span><span class="price">5,5</span></div>
    <div class="item"><span>Brotkorb mit<br>Knoblauchbutter</span><span class="price">2,5</span></div>
    <div class="item item--small"><span>Pesto Basilico</span><span class="price">1,5</span></div>
    <div class="item item--small"><span>Tomatenpesto</span><span class="price">1,5</span></div>
    <div class="item item--small"><span>Chimichurri</span><span class="price">1,5</span></div>
    <div class="item item--small"><span>Aioli</span><span class="price">1,5</span></div>
    <div class="item item--small"><span>Pico de Gallo</span><span class="price">1,5</span></div>
    <div class="item item--small"><span>Oliventapenade</span><span class="price">1,5</span></div>
    <div class="item item--small"><span>Hummus</span><span class="price">1,5</span></div>
    <div class="item"><span>Gewürzte Oliven</span><span class="price">2,5</span></div>
    <div class="item item--small"><span>Karotten</span><span class="price">2</span></div>
    <p class="desc">Mit aromatischen Kräutern in Weißwein, Essig und Kümmel</p>
    <div class="item"><span>Papas Arrugadas</span><span class="price">4</span></div>
    <p class="desc">kanarische Salzkartoffeln</p>
    <div class="item"><span>Wurst &amp; Käsebrett</span><span class="price">7,5</span></div>
    <p class="desc">Schinken und Wurst aus der Region, Edamer, Brie &amp; Obazda</p>
    <div class="item"><span>Kroketten</span><span class="price">2,5</span></div>
    <p class="desc">Stockfisch-Kroketten, Samosa oder Fleisch &amp; Garnelen-Pastete</p>
    <div class="item"><span>Pimientos del Piquillo</span><span class="price">3,5</span></div>
    <div class="item"><span>Pimientos de Padrón</span><span class="price">4,5</span></div>
    <div class="item"><span>Bruschetta Pico-de-Gallo</span><span class="price">6,5</span></div>
    <p class="desc">geröstetes Knoblauchbrot mit marinierter Tomaten-Gurken Salsa</p>
    <div class="item"><span>Obazda</span><span class="price">4,5</span></div>
    <p class="desc">mit Breze &amp; roten Zwiebeln</p>
    <div class="item"><span>Büffelmozzarella</span><span class="price">10,5</span></div>
    <p class="desc">Mit Tomate, Rucola und Balsamicocreme</p>
    <div class="item"><span>Antipasti-Spieße</span><span class="price">5</span></div>
    <p class="desc">Zucchini, Kirschtomaten, rote Zwiebeln, Paprika, Mozzarella</p>
  </div>

  <div class="col" style="left:297px;top:290px;width:162px">
    <div class="item"><span>Gegrillter Ziegenkäse</span><span class="price">6,5</span></div>
    <p class="desc">Paniert mit Marmelade und Walnüssen</p>
    <div class="gap"></div>
    <div class="item"><span>Huevos Rancheros</span><span class="price">9</span></div>
    <p class="desc">Würzige Kombination aus Tomaten-Eintopf mit pochiertem Ei, garniert mit Pico de Gallo</p>
    <h2 class="section" style="margin-top:10px">FLEISCH</h2>
    <div class="item"><span>Pflaumen im Speckmantel</span><span class="price">4</span></div>
    <div class="item"><span>Chorizo</span><span class="price">5,5</span></div>
    <p class="desc">gegrillte pikante Paprikawurst aus Spanien</p>
    <div class="item"><span>Albóndigas</span><span class="price">5,5</span></div>
    <p class="desc">Saftige Wild-Fleischbällchen in Tomatensauce</p>
    <div class="item"><span>Cassoulet 7,5</span><span class="price"></span></div>
    <p class="desc">Bohneneintopf mit regionalem Fleisch und würziger Chorizo</p>
    <h2 class="section" style="margin-top:10px">FISCH</h2>
    <div class="item"><span>Boquerones en Vinagre</span><span class="price">6</span></div>
    <p class="desc">In Olivenöl und Weinessig eingelegte Sardellenfilets, mit Knoblauch und Petersilie</p>
    <div class="item"><span>Knusprige Garnelen</span><span class="price">7,5</span></div>
    <p class="desc">Tempura-Panko Panade Garnelen mit hausgemachter Aioli</p>
    <div class="item"><span>Gambas Pil Pil.</span><span class="price">7,5</span></div>
    <p class="desc">Garnelen mit Knoblauch und Chili</p>
  </div>

  <div class="photo" role="img" aria-label="Foto: Oliven, Tomaten und Kräuter auf Holzbrett" style="left:0;top:617px;width:66px;height:143px;background:radial-gradient(circle at 30% 70%,#6f7a2a 0,#3f4a1c 30%,transparent 70%),linear-gradient(180deg,transparent,#3a2a1c)"></div>
  <div class="photo" role="img" aria-label="Foto: Schale mit glasierten Garnelen und Koriander" style="left:335px;top:572px;width:202px;height:188px;background:radial-gradient(ellipse 80px 70px at 52% 58%,#d2702d 0%,#a4461c 55%,#2a1a12 80%,transparent 100%),linear-gradient(135deg,transparent 30%,#3b2718 100%)"></div>
</section>

<section class="sheet sheet--main" aria-label="Hauptspeise">
  <div class="photo" role="img" aria-label="Foto: Hähnchenspieße mit Paprika auf schwarzem Teller" style="left:155px;top:0;width:295px;height:181px;background:radial-gradient(ellipse 110px 45px at 55% 55%,#e3b9a0 0%,#b5563f 45%,#2b2b2d 90%),linear-gradient(180deg,#3a3a3c,#1f1f21)"></div>
  <h1 class="sheet-title" style="top:200px">Hauptspeise</h1>
  <div class="title-rule" style="left:146px;width:238px;top:243px"></div>
  <p class="hours" style="top:248px">Von 19:00 bis 22:00 Uhr</p>

  <div class="col" style="left:76px;top:280px;width:157px">
    <div class="item"><span>Hähnchen nach Art<br>des Hauses</span><span class="price">12,5</span></div>
    <p class="desc">Hähnchen in Olivenöl mit Knoblauch gegrillt, belegt mit Mini-Pickles, Oliven und Koriander</p>
    <div class="gap"></div>
    <h2 class="section">RINDERFILET /G</h2>
    <h2 class="section" style="margin-top:6px">BEEF TAGLIATA /G</h2>
    <div class="gap--tight"></div>
    <div class="item"><span>Cassoulet</span><span class="price">14</span></div>
    <p class="note" style="margin:5px 0 0 2px">Nur auf Vorbestellung<br>ab 2 Personen</p>
    <div class="gap--tight"></div>
    <div class="item"><span>Cataplana</span><span class="price">45</span></div>
    <p class="note" style="font-size:10px;line-height:1.25">mit Meeresfrüchten<br>mit Seeteufel/Seebarsch<br>mit Kabeljau</p>
    <div class="gap--tight"></div>
    <div class="item"><span>Schweinefleisch und<br>Muscheln</span><span class="price">40</span></div>
    <div class="gap--tight"></div>
    <div class="item"><span>Oktopus à Lagareiro</span><span class="price">45</span></div>
    <div class="gap--tight"></div>
    <div class="item"><span>Entenreis</span><span class="price">35</span></div>
  </div>

  <div class="col" style="left:300px;top:282px;width:150px">
    <h2 class="section" style="text-decoration:none">KINDER MENU</h2>
    <div class="item"><span>Spaghetti mit<br>Fleischbällchen</span><span class="price">7,5</span></div>
    <h2 class="section" style="margin-top:12px">BEILAGEN</h2>
    <div class="item item--small"><span>Bunter Gartensalat</span><span class="price">3,5</span></div>
    <div class="item item--small"><span>Tomatensalat</span><span class="price">2,5</span></div>
    <div class="item item--small"><span>Tageskartoffelbeilage</span><span class="price">2,5</span></div>
    <div class="item item--small"><span>Rustikale Kartoffelchips</span><span class="price">2</span></div>
    <div class="item item--small"><span>Süßkartoffelpommes</span><span class="price">2,5</span></div>
    <div class="item item--small"><span>Reis</span><span class="price"></span></div>
  </div>

  <div class="photo" role="img" aria-label="Foto: Meeresfrüchte-Eintopf mit Garnelen, Krabbe, Limette und Chili, daneben Knoblauch und Tomate" style="left:13px;top:456px;width:524px;height:304px;background:radial-gradient(ellipse 170px 150px at 75% 60%,#d6692c 0%,#b4471f 40%,#4a2418 75%,transparent 100%),radial-gradient(circle at 16% 64%,#cfc6b8 0 18px,transparent 20px),radial-gradient(circle at 12% 90%,#b8261a 0 14px,transparent 16px),radial-gradient(ellipse 45px 25px at 50% 100%,#e8d68a 0,transparent 100%),linear-gradient(180deg,rgba(28,28,30,1) 0%,rgba(40,34,34,.8) 25%,#2c2628 100%)"></div>
</section>

</body>
</html>
```